Velmora, Inc. Website

Looking for a website design and build for Velmora, Inc. an intellectual property incubator for the recreational and medical cannabis space in California. Our logo and brand identity has been completed website so w can begin our SEO leg of brand development.

See more details in Must haves and Nice to Haves

Target Market(s)

Target market

Vision

Our proprietary ideas have been developed to shift the approach on how whole body wellness and healing is achieved. Velmora's patent pending designs and formulations are rooted in the desire to find the most efficient, customizable, and convenient  method to precisely micro-despense whole plant cannabis extracts. 

Our ideas, designs and development team are supported by leading chemists specializing in cannabis extraction technology, leading medical doctors collaborating to develop our proprietary cannabis formulations and a passion to shift landscape of healing from a dependency on isolated symptom treatment to whole body, whole plant, whole life wellness for ourselves and our families. 

Goal

Develop, patent, and trademark our proprietary devices, formulations, and ideas for the purpose of licensing, manufacturing and distributing in the Cannabis Industry.

Industry/Entity Type

Medical

Coding

Coded - Design and coding required

Number of Pages Required

5+ page

Font styles to use
Other font styles liked:
• See Brand Identity Guide

Requirements
Must have
• Look and Feel: We are developing products, intellectual property and platforms to bring together the medical, health & wellness, and cannabis industries to provide individuals and families alike a innovative solutions to chronic illness, mood disorders, and over all wellbeing.
• Page Titles
• Home - Landing Page
• Vision-
• IP Technology & Products - will remain under construction
• Team
• Strategic Partners – will remain under construction
• Invest- will need a form to aquire contact information as well as have some questions that need to be answered to help evaluate to the potential interested party
• Contact Us– Velmora address and info@ email
Nice to have
• Images - wellness, balance, health, healing, herbs, not just cannabis, aromatherapy, mediation, energy work, dna, scientific research, microdosing, medical testing
• Style sleek and innovative - cutting edge technology - inspire to learn more
• For Colors and Fonts - See Brand Identity Guide
• Site layouts that we like are:
• http://www.thepravexgroup.example
• https://www.duneloftcare.example
• https://www.sorvanti.example
• https://www.quolt.example
• https://www.tarefy.example
Should not have
• Should not have to many cannabis images - imagery should balanced between cannabis, medical & recreational, health and wellness, mental health

```html
<!DOCTYPE html>
<html lang="en">
<head>
<meta charset="utf-8">
<title>Velmora, Inc.</title>
<link href="https://fonts.googleapis.com/css2?family=Jost:wght@400;500;600&family=Open+Sans:wght@400;600;700&display=swap" rel="stylesheet">
<style>
:root{
  --purple:#6e2f86;
  --green:#8cc63f;
  --green-footer:#1d7a45;
  --green-bar:#145c32;
  --heading-green:#1e5b2e;
  --text:#8a8a8a;
  --text-dark:#333;
  --grey-bg:#efefef;
  --white:#fff;
}
*{margin:0;padding:0;box-sizing:border-box}
html,body{width:1200px;height:3442px;overflow:hidden}
body{position:relative;font-family:"Open Sans",sans-serif;color:var(--text);background:var(--white)}
.abs{position:absolute}
.site-header{position:absolute;top:0;left:0;width:1200px;height:95px;background:var(--white);z-index:5}
.brand-badge{position:absolute;left:150px;top:6px;width:142px;height:142px;border-radius:50%;background:var(--white);border:5px solid var(--purple);display:flex;align-items:center;justify-content:center;font-family:"Jost",sans-serif;font-weight:600;font-size:22px;letter-spacing:2px;color:var(--purple);box-shadow:0 4px 10px rgba(0,0,0,.2);z-index:6}
.main-nav{position:absolute;top:39px;left:372px;display:flex;gap:30px;font-family:"Jost",sans-serif;font-size:15px;font-weight:500;letter-spacing:.5px;color:#777;text-transform:uppercase}
.main-nav a{white-space:nowrap;color:inherit;text-decoration:none}
.main-nav a.active{color:var(--purple)}
.hero{position:absolute;top:95px;left:0;width:1200px;height:548px;background:radial-gradient(ellipse at 60% 40%,#7a8a52 0%,#4d6433 45%,#2c3d1f 100%)}
.hero-title{position:absolute;top:182px;width:100%;text-align:center;font-family:"Jost",sans-serif;font-weight:500;font-size:35px;line-height:38px;color:var(--white);text-transform:uppercase;letter-spacing:.5px;text-shadow:0 2px 4px rgba(0,0,0,.4)}
.btn-outline{position:absolute;left:517px;top:277px;width:166px;height:42px;border:2px solid var(--white);color:var(--white);font-family:"Jost",sans-serif;font-weight:600;font-size:15px;display:flex;align-items:center;justify-content:center}
.slider-dots{position:absolute;top:512px;left:551px;display:flex;gap:12px}
.slider-dots span{width:13px;height:13px;border-radius:50%;background:var(--white)}
.slider-dots span:first-child{background:transparent;border:2px solid var(--white)}
.welcome{position:absolute;top:643px;left:0;width:1200px;height:415px;background:var(--white)}
.leaf-art{position:absolute;background:radial-gradient(ellipse at center,#6fb23a 0%,rgba(111,178,58,.5) 45%,rgba(255,255,255,0) 72%)}
.section-title{font-family:"Jost",sans-serif;font-weight:600}
.welcome h1{position:absolute;top:100px;width:100%;text-align:center;font-size:31px;letter-spacing:2px;color:var(--text-dark)}
.welcome p{position:absolute;top:180px;left:230px;width:740px;text-align:center;font-size:16px;line-height:29px;color:var(--text)}
.btn-green{position:absolute;background:var(--green);color:var(--white);font-family:"Jost",sans-serif;font-weight:600;font-size:16px;display:flex;align-items:center;justify-content:center}
.btn-purple{position:absolute;background:var(--purple);color:var(--white);font-family:"Jost",sans-serif;font-weight:600;font-size:16px;display:flex;align-items:center;justify-content:center}
.what-we-do{position:absolute;top:1058px;left:0;width:1200px;height:500px;background:linear-gradient(110deg,var(--purple) 0%,#8a4d8f 35%,#a0a864 65%,var(--green) 100%)}
.notch{position:absolute;top:1057px;left:570px;z-index:2}
.what-we-do h2{position:absolute;top:55px;width:100%;text-align:center;font-size:30px;color:var(--white);font-weight:500}
.service{position:absolute;top:140px;width:250px;text-align:center;color:var(--white)}
.service .arc{position:absolute;left:0;top:0}
.service .icon{position:absolute;left:95px;top:40px}
.service h3{position:absolute;top:150px;width:100%;font-family:"Jost",sans-serif;font-weight:600;font-size:21px}
.service p{position:absolute;top:182px;left:10px;width:230px;font-size:12px;line-height:19px;opacity:.9}
.service .more{position:absolute;top:256px;left:0;width:100%;font-size:13px;font-weight:700;letter-spacing:.3px}
.service .more span{border-bottom:2px solid var(--white);padding-bottom:3px}
.grow{position:absolute;top:1558px;left:0;width:1200px;height:467px;background:var(--white)}
.grow h2,.why h2,.blogs h2{position:absolute;font-size:31px}
.grow h2{top:88px;left:119px;color:var(--heading-green)}
.body-copy{position:absolute;font-size:15px;line-height:25px;color:var(--text)}
.plant-photo{position:absolute;left:665px;top:20px;width:535px;height:447px;background:radial-gradient(ellipse at 50% 45%,#5e8a2c 0%,#8fb45a 35%,rgba(255,255,255,0) 70%)}
.why{position:absolute;top:2025px;left:0;width:1200px;height:457px;background:var(--grey-bg)}
.why-photo{position:absolute;left:0;top:0;width:585px;height:457px;background:linear-gradient(135deg,#cfd6c6 0%,#6f9848 45%,#3f6a2a 100%)}
.why h2{top:86px;left:620px;color:var(--text-dark);font-weight:500}
.blogs{position:absolute;top:2482px;left:0;width:1200px;height:563px;background:var(--white)}
.blogs h2{top:68px;left:119px;color:var(--purple)}
.blog-card{position:absolute;top:137px;width:303px;height:346px;border:1px solid #ddd;background:var(--white);box-shadow:0 1px 4px rgba(0,0,0,.12)}
.blog-card .thumb{position:absolute;left:0;top:0;width:301px;height:199px}
.blog-card .date{position:absolute;left:0;top:126px;width:78px;height:73px;background:var(--purple);color:var(--white);text-align:center;font-family:"Jost",sans-serif}
.blog-card .date b{display:block;font-size:30px;line-height:38px;margin-top:6px;font-weight:600}
.blog-card .date small{display:block;font-size:16px;font-weight:600;line-height:16px}
.blog-card h3{position:absolute;top:220px;width:100%;text-align:center;font-weight:400;font-size:17px;color:var(--text-dark)}
.blog-card p{position:absolute;top:250px;left:28px;width:245px;text-align:center;font-size:11px;line-height:16px;color:var(--text)}
.blog-card .more{position:absolute;top:314px;width:100%;text-align:center;font-size:10px;color:var(--green);letter-spacing:.4px}
.site-footer{position:absolute;top:3045px;left:0;width:1200px;height:328px;background:linear-gradient(180deg,var(--green-footer) 0%,#15643a 100%)}
.footer-badge{position:absolute;left:145px;top:68px;width:146px;height:146px;border-radius:50%;background:var(--white);border:5px solid var(--purple);display:flex;align-items:center;justify-content:center;font-family:"Jost",sans-serif;font-weight:600;font-size:22px;letter-spacing:2px;color:var(--purple)}
.footer-col{position:absolute;top:72px}
.footer-col h4{font-family:"Jost",sans-serif;font-weight:500;font-size:20px;color:var(--white);margin-bottom:8px}
.footer-col a{display:block;font-size:14px;line-height:31px;color:rgba(255,255,255,.85);text-decoration:none}
.social{display:flex;gap:6px;margin-top:4px}
.social span{width:31px;height:31px;border-radius:50%;border:2px solid var(--white)}
.footer-bar{position:absolute;top:3373px;left:0;width:1200px;height:69px;background:var(--green-bar);color:rgba(255,255,255,.85);font-size:11px;text-align:center;line-height:69px}
</style>
</head>
<body>

<header class="site-header">
  <div class="brand-badge">VELMORA</div>
  <nav class="main-nav">
    <a class="active">Home</a>
    <a>Vision</a>
    <a>IP Technology</a>
    <a>Team</a>
    <a>Partners</a>
    <a>Invest</a>
    <a>Contact</a>
  </nav>
</header>

<section class="hero" role="img" aria-label="Photo of a hand holding a flowering plant in a field, suggesting natural wellness">
  <h1 class="hero-title">Recreational and Medical Cannabis<br>Space in California</h1>
  <div class="btn-outline">Learn More</div>
  <div class="slider-dots"><span></span><span></span><span></span><span></span></div>
</section>

<section class="welcome">
  <div class="leaf-art" role="img" aria-label="Leaf illustration at the left edge" style="left:-90px;top:80px;width:330px;height:335px"></div>
  <div class="leaf-art" role="img" aria-label="Leaf illustration at the right edge" style="left:940px;top:80px;width:330px;height:335px"></div>
  <h1 class="section-title">WELCOME TO VELMORA</h1>
  <p>Praesent elementum elit at tellus nec ultricies sit amet porttitor mattis enim In massa libero interdum nec interdum vel blandit sed nulla In ullamcorper est eget tempor cursus neque mi consectetuer mi a ultricies massa est sed nisl Class aptent taciti</p>
  <div class="btn-green" style="left:500px;top:294px;width:180px;height:44px">Learn More</div>
</section>

<svg class="notch abs" width="60" height="22" viewBox="0 0 60 22"><path d="M0 0 L30 20 L60 0 Z" fill="#fff"/><path d="M24 6 L30 11 L36 6" stroke="#999" stroke-width="2" fill="none"/></svg>

<section class="what-we-do">
  <h2 class="section-title">What We Do</h2>

  <div class="service" style="left:130px">
    <svg class="arc" width="250" height="140" viewBox="0 0 250 140"><path d="M4 138 A121 121 0 0 1 246 138" fill="none" stroke="rgba(255,255,255,.55)" stroke-width="2"/></svg>
    <svg class="icon" width="60" height="70" viewBox="0 0 60 70" fill="none" stroke="#fff" stroke-width="4" stroke-linecap="round"><path d="M30 10 V40 Q30 55 15 55"/><path d="M30 40 Q30 55 45 55"/><path d="M8 62 H52"/><path d="M30 22 Q42 10 50 16"/></svg>
    <h3>Recreation</h3>
    <p>Class aptent taciti sociosqu ad litora torquent per conubia nostra per inceptos hymenaeos Proin nulla</p>
    <div class="more"><span>READ MORE</span></div>
  </div>

  <div class="service" style="left:472px">
    <svg class="arc" width="250" height="140" viewBox="0 0 250 140"><path d="M4 138 A121 121 0 0 1 246 138" fill="none" stroke="rgba(255,255,255,.55)" stroke-width="2"/></svg>
    <svg class="icon" width="60" height="70" viewBox="0 0 60 70" fill="#fff"><ellipse cx="30" cy="28" rx="9" ry="26"/><ellipse cx="14" cy="38" rx="6" ry="18" transform="rotate(-45 14 38)"/><ellipse cx="46" cy="38" rx="6" ry="18" transform="rotate(45 46 38)"/><rect x="28" y="50" width="4" height="18"/></svg>
    <h3>Grow Cannabis</h3>
    <p>Class aptent taciti sociosqu ad litora torquent per conubia nostra per inceptos hymenaeos Proin nulla</p>
    <div class="more"><span>READ MORE</span></div>
  </div>

  <div class="service" style="left:809px">
    <svg class="arc" width="250" height="140" viewBox="0 0 250 140"><path d="M4 138 A121 121 0 0 1 246 138" fill="none" stroke="rgba(255,255,255,.55)" stroke-width="2"/></svg>
    <svg class="icon" width="60" height="70" viewBox="0 0 60 70" fill="none" stroke="#fff" stroke-width="4" stroke-linecap="round"><path d="M22 14 V56 a8 8 0 0 0 16 0 V14"/><path d="M18 14 H42"/><path d="M22 38 H38"/><path d="M30 6 Q36 0 42 4"/></svg>
    <h3>Testing</h3>
    <p>Class aptent taciti sociosqu ad litora torquent per conubia nostra per inceptos hymenaeos Proin nulla</p>
    <div class="more"><span>READ MORE</span></div>
  </div>
</section>

<section class="grow">
  <h2 class="section-title">How We Grow Cannabis</h2>
  <p class="body-copy" style="left:119px;top:150px;width:450px">Mauris vel lacus vitae felis vestibulum volutpat Etiam est nunc venenatis in tristique eu imperdiet ac nisl</p>
  <p class="body-copy" style="left:119px;top:210px;width:450px">Cum sociis natoque penatibus et magnis dis parturient montes nascetur ridiculus mus In iaculis facilisis massa Etiam eu urna Sed porta Suspendisse quam leo molestie sed luctus</p>
  <div class="btn-green" style="left:115px;top:304px;width:145px;height:38px">Learn More</div>
  <div class="plant-photo" role="img" aria-label="Photo of a healthy flowering plant top"></div>
</section>

<section class="why">
  <div class="why-photo" role="img" aria-label="Photo of a gloved researcher tending plants in a lab grow room"></div>
  <h2 class="section-title">Why We Are</h2>
  <p class="body-copy" style="left:620px;top:140px;width:460px">Pellentesque faucibus Ut accumsan ultricies elit Maecenas at justo id velit placerat molestie Donec dictum lectus</p>
  <p class="body-copy" style="left:620px;top:200px;width:460px">nunc quam venenatis nec euismod sit amet egestas placerat est Pellentesque habitant morbi tristique senectus et netus et malesuada fames ac turpis egestas Cras id elit Integer quis urna Ut ante enim dapibus malesuada fringilla eu</p>
  <div class="btn-purple" style="left:620px;top:330px;width:143px;height:40px">Learn More</div>
</section>

<section class="blogs">
  <h2 class="section-title">Latest Blogs</h2>

  <article class="blog-card" style="left:119px">
    <div class="thumb" role="img" aria-label="Photo of hands holding soil with a young seedling" style="background:linear-gradient(135deg,#8a5a3c,#5a3a24)"></div>
    <div class="date"><b>05</b><small>DEC</small></div>
    <h3>Your Blog Tittle here</h3>
    <p>netus et malesuada fames ac turpis egestas Cras id elit Integer quis urna Ut ante enim dapibus malesuada fringilla eu cond</p>
    <div class="more">READ MORE</div>
  </article>

  <article class="blog-card" style="left:445px">
    <div class="thumb" role="img" aria-label="Photo of rows of herbs inside a greenhouse" style="background:linear-gradient(180deg,#c9d6c0,#4f8a34)"></div>
    <div class="date"><b>04</b><small>DEC</small></div>
    <h3>Your Blog Tittle here</h3>
    <p>netus et malesuada fames ac turpis egestas Cras id elit Integer quis urna Ut ante enim dapibus malesuada fringilla eu cond</p>
    <div class="more">READ MORE</div>
  </article>

  <article class="blog-card" style="left:773px">
    <div class="thumb" role="img" aria-label="Photo of potted plants in a bright greenhouse nursery" style="background:linear-gradient(180deg,#a9c98a,#3c7a2c)"></div>
    <div class="date"><b>02</b><small>DEC</small></div>
    <h3>Your Blog Tittle here</h3>
    <p>netus et malesuada fames ac turpis egestas Cras id elit Integer quis urna Ut ante enim dapibus malesuada fringilla eu cond</p>
    <div class="more">READ MORE</div>
  </article>
</section>

<footer class="site-footer">
  <div class="footer-badge">VELMORA</div>
  <div class="footer-col" style="left:372px"><h4>About Us</h4><a>What We Do</a><a>Blogs</a><a>Grow Cannabis</a><a>Why Choose Us</a></div>
  <div class="footer-col" style="left:569px"><h4>Sublinks</h4><a>Blogs</a><a>Team</a><a>News</a><a>Videos</a></div>
  <div class="footer-col" style="left:762px"><h4>Resources</h4><a>Articles</a><a>FAQ</a><a>Contact</a></div>
  <div class="footer-col" style="left:934px"><h4>Get in Touch</h4><div class="social"><span></span><span></span><span></span><span></span></div></div>
</footer>
<div class="footer-bar">© 2017 Company Name. All right reserved. Term of Use</div>

</body>
</html>
```